Veltrano Community Development Planning New web site

Design a new web site. I have a budget of $1,500.00.
Attached on PowerPoint is a complete site plan. Home page and linked pages.
10 - 12 pages. All copy and photos will be supplied. (300dpi)
I have shown them the concept which they like.
No data bases required. Home page with animations dissolving.
They former web site has been taken down. They have been in business 30 years in New Jersey
Colors teal blues and greens
There will be a new logo)being designed)
The text in home page copy will give you a detailed story what they are all about.

files have been approved for Veltrano, Inc.   Tomas is the designer

Industry/Entity Type

Community

```html
<!DOCTYPE html>
<html lang="en">
<head>
<meta charset="UTF-8">
<title>Veltrano Community Development Planning</title>
<link rel="stylesheet" href="https://fonts.googleapis.com/css2?family=Source+Sans+3:wght@300;400;600;700&display=swap">
<style>
  :root {
    --header-bg: #25323c;
    --brand-green: #6dd54f;
    --nav-text: #ffffff;
    --nav-active-bg: #f4f4f4;
    --caption-bg: #ffffff;
    --caption-text: #555c61;
    --hero-a: #c9c3bb;
    --hero-b: #a98a6a;
    --hero-c: #7f8a96;
  }
  * { box-sizing: border-box; margin: 0; padding: 0; }
  html, body { width: 1200px; height: 619px; overflow: hidden; }
  body { font-family: "Source Sans 3", "Source Sans Pro", sans-serif; background: var(--header-bg); position: relative; }

  .site-header {
    position: absolute; left: 0; top: 0; width: 1200px; height: 103px;
    background: var(--header-bg);
  }
  .brand {
    position: absolute; left: 75px; top: 36px;
    font-size: 27px; font-weight: 700; letter-spacing: 1px;
    color: var(--brand-green); text-transform: uppercase; line-height: 1;
  }
  .main-nav a {
    position: absolute; top: 44px; font-size: 12px; font-weight: 600;
    color: var(--nav-text); text-decoration: none; text-transform: uppercase;
    line-height: 14px; white-space: nowrap;
  }
  .main-nav .is-active {
    top: 37.5px; height: 26.5px; padding: 6px 9px 0;
    background: var(--nav-active-bg); color: var(--brand-green); border-radius: 1px;
  }
  .main-nav .is-active::after {
    content: ""; position: absolute; left: 50%; bottom: -5px; margin-left: -6px;
    border-left: 6px solid transparent; border-right: 6px solid transparent;
    border-top: 6px solid var(--nav-active-bg);
  }

  .hero {
    position: absolute; left: 0; top: 103px; width: 1200px; height: 516px;
    background:
      radial-gradient(ellipse at 45% 45%, var(--hero-b) 0%, transparent 45%),
      linear-gradient(100deg, var(--hero-a) 0%, #d8d4cf 45%, var(--hero-c) 85%, #6e6760 100%);
  }
  .hero-caption-title {
    position: absolute; left: 731px; top: 432px; width: 394px; height: 49px;
    background: var(--brand-green); color: #ffffff;
    font-size: 23px; font-weight: 600; line-height: 49px; padding-left: 18px;
  }
  .hero-caption-text {
    position: absolute; left: 731px; top: 490px; width: 366px; height: 49px;
    background: var(--caption-bg); color: var(--caption-text);
    font-size: 23px; font-weight: 300; line-height: 49px; padding-left: 18px;
  }
</style>
</head>
<body>
  <header class="site-header">
    <div class="brand">Veltrano</div>
    <nav class="main-nav">
      <a href="#" style="left:410px">Home</a>
      <a href="#" class="is-active" style="left:483px">Our Company</a>
      <a href="#" style="left:602px">Services</a>
      <a href="#" style="left:682px">Housing Rehab Application</a>
      <a href="#" style="left:873px">Affordable Application</a>
      <a href="#" style="left:1057px">Contact Us</a>
    </nav>
  </header>

  <section class="hero" role="img" aria-label="Photo of a couple on a sofa reviewing house plans with an advisor">
  </section>
  <div class="hero-caption-title">Lakewood Community Members</div>
  <div class="hero-caption-text">Apply today for your rehab grant!</div>
</body>
</html>
```